Bref créative
Holloway & Daughters
Biz Card/Stationery
I need single sided standard sized Business Card [3.5" x 2"]
Spinnaker Font and what's in logo
Professional
Derek Fulton
Vice President, Operations
3172 W. Maple Boulevard
Indianapolis, IN
dfulton@hollowaydaughters.com
hollowaydaughters.com

```html
<!DOCTYPE html>
<html lang="en">
<head>
<meta charset="utf-8">
<title>Holloway &amp; Daughters – Business Card</title>
<link href="https://fonts.googleapis.com/css2?family=Spinnaker&display=swap" rel="stylesheet">
<style>
  :root {
    --gold: #c9a135;
    --ink: #2b2b2b;
    --muted: #6d6d6d;
    --paper: #ffffff;
    --backdrop: #ecebe8;
    --rule: #d9c287;
  }
  html, body {
    margin: 0;
    width: 1200px;
    height: 630px;
    overflow: hidden;
    background: var(--backdrop);
    font-family: "Spinnaker", sans-serif;
  }
  .sheet {
    width: 1200px;
    height: 630px;
    display: flex;
    align-items: center;
    justify-content: center;
    gap: 60px;
  }
  .card {
    width: 525px;
    height: 300px;
    position: relative;
    box-shadow: 0 6px 18px rgba(0,0,0,0.12);
    box-sizing: border-box;
  }
  .card--front {
    background: var(--gold);
    display: flex;
    align-items: center;
    justify-content: center;
  }
  .brand-name {
    font-size: 30px;
    letter-spacing: 1px;
    text-transform: uppercase;
    text-align: center;
    line-height: 1.15;
    margin: 0;
  }
  .card--front .brand-name { color: var(--paper); }
  .card--back {
    background: var(--paper);
    display: flex;
    align-items: center;
  }
  .back-brand {
    width: 52%;
    display: flex;
    justify-content: center;
  }
  .card--back .brand-name { color: var(--ink); font-size: 26px; }
  .divider {
    width: 1px;
    height: 170px;
    background: var(--rule);
  }
  .contact {
    padding-left: 22px;
    color: var(--muted);
    font-size: 11.5px;
  }
  .contact-name {
    color: var(--gold);
    font-size: 17px;
    margin: 0 0 2px;
  }
  .contact-title {
    margin: 0 0 16px;
    font-size: 11px;
    text-transform: uppercase;
    letter-spacing: 0.5px;
  }
  .contact-list { list-style: none; margin: 0; padding: 0; }
  .contact-list li {
    display: flex;
    align-items: flex-start;
    gap: 8px;
    margin-bottom: 7px;
    line-height: 1.3;
  }
  .contact-list svg { flex: none; margin-top: 1px; }
</style>
</head>
<body>
<main class="sheet">
  <section class="card card--front">
    <h1 class="brand-name">Holloway &amp;<br>Daughters</h1>
  </section>

  <section class="card card--back">
    <div class="back-brand">
      <h2 class="brand-name">Holloway &amp;<br>Daughters</h2>
    </div>
    <div class="divider"></div>
    <div class="contact">
      <p class="contact-name">Derek Fulton</p>
      <p class="contact-title">Vice President, Operations</p>
      <ul class="contact-list">
        <li>
          <svg width="12" height="12" viewBox="0 0 12 12"><path d="M6 0.5a4 4 0 0 0-4 4c0 3 4 7 4 7s4-4 4-7a4 4 0 0 0-4-4zm0 5.5a1.5 1.5 0 1 1 0-3 1.5 1.5 0 0 1 0 3z" fill="var(--gold)"/></svg>
          <span>3172 W. Maple Boulevard<br>Indianapolis, IN</span>
        </li>
        <li>
          <svg width="12" height="12" viewBox="0 0 12 12"><path d="M2.5 1h2l1 2.5-1.3 1a6 6 0 0 0 3.3 3.3l1-1.3 2.5 1v2a1 1 0 0 1-1 1A9.5 9.5 0 0 1 1.5 2a1 1 0 0 1 1-1z" fill="var(--gold)"/></svg>
          <span>(317) 555-0148</span>
        </li>
        <li>
          <svg width="12" height="12" viewBox="0 0 12 12"><rect x="0.5" y="2" width="11" height="8" rx="1" fill="var(--gold)"/><path d="M1 2.8l5 3.6 5-3.6" stroke="#fff" stroke-width="1" fill="none"/></svg>
          <span>dfulton@hollowaydaughters.com</span>
        </li>
        <li>
          <svg width="12" height="12" viewBox="0 0 12 12"><circle cx="6" cy="6" r="5" fill="none" stroke="var(--gold)" stroke-width="1.2"/><path d="M1 6h10M6 1c-2.5 3-2.5 7 0 10M6 1c2.5 3 2.5 7 0 10" stroke="var(--gold)" stroke-width="1" fill="none"/></svg>
          <span>hollowaydaughters.com</span>
        </li>
      </ul>
    </div>
  </section>
</main>
</body>
</html>
```